Dorsey K. Wendell Business Card

We need a business card for our company Dorsey K. Wendell Heating & Plumbing to be distributed to potential customers. It should follow the color scheme of our logo and have a modern upscale and masculine look.

The logo is attached and the info below should also be included:

5187 W. Cedar Brook Rd.
Harlow Springs, PA 16924

Russell T. Wendell
(717) 592-0817
russelltwendell@fernmail.net
dorseykwendell.net
PA #093148

Industry/Entity Type

Business

Contact Information for Business Card

5187 W. Cedar Brook Rd.
Harlow Springs, PA 16924

Russell T. Wendell
(717) 592-0817
russelltwendell@fernmail.net
dorseykwendell.net
PA #093148

Colors

Designer to choose colors to be used in the design.

Requirements
Must have
• Information above included

```html
<!DOCTYPE html>
<html lang="en">
<head>
<meta charset="utf-8">
<title>Dorsey K. Wendell Business Card</title>
<link rel="stylesheet" href="https://fonts.googleapis.com/css2?family=Open+Sans:wght@400;700;800&display=swap">
<style>
  :root {
    --navy: #1f1d5e;
    --brand-blue: #1b5fb5;
    --teal: #66c4d1;
    --aqua-pale: #dcf0f4;
    --aqua-mid: #9fd3de;
    --paper: #ffffff;
    --backdrop: #e6e8ea;
  }
  * { box-sizing: border-box; margin: 0; padding: 0; }
  html, body {
    width: 1200px; height: 1200px; overflow: hidden;
    background: var(--backdrop);
    font-family: "Open Sans", Arial, sans-serif;
  }
  .sheet {
    width: 1200px; height: 1200px;
    display: flex; flex-direction: column; align-items: center; justify-content: center;
    gap: 60px;
  }
  .card {
    position: relative;
    width: 840px; height: 480px;
    overflow: hidden;
    background: var(--paper);
    box-shadow: 0 6px 18px rgba(0,0,0,0.12);
  }

  /* Front */
  .card-front__photo {
    position: absolute; inset: 0;
    background:
      radial-gradient(ellipse at 70% 55%, var(--aqua-mid) 0%, transparent 45%),
      linear-gradient(180deg, #eaf6f8 0%, var(--aqua-pale) 60%, #bfe3ea 100%);
  }
  .card-front__panel {
    position: absolute; inset: 0; width: 840px; height: 480px;
  }
  .card-front__panel polygon { fill: var(--navy); }
  .contact {
    position: absolute; left: 56px; top: 150px;
    color: var(--paper);
    font-size: 18px; line-height: 1.45; font-weight: 400;
  }
  .contact__address { margin-bottom: 22px; }
  .brand-lockup {
    position: absolute; right: 36px; top: 66px;
    display: flex; align-items: center; gap: 12px;
  }
  .brand-lockup__mark {
    width: 38px; height: 38px; background: var(--brand-blue);
  }
  .brand-lockup__name {
    color: var(--navy);
    font-size: 26px; font-weight: 800; letter-spacing: 0.5px;
    text-transform: uppercase; white-space: nowrap;
  }

  /* Back */
  .card-back__band {
    position: absolute; left: 0; right: 0; bottom: 0; height: 58%;
    background: var(--teal);
  }
  .card-back__lockup {
    position: absolute; left: 50%; top: 42%;
    transform: translate(-50%, -50%);
    display: flex; align-items: center; gap: 16px;
  }
  .card-back__mark { width: 48px; height: 48px; background: var(--brand-blue); }
  .card-back__name {
    color: var(--navy);
    font-size: 40px; font-weight: 800; letter-spacing: 1px;
    text-transform: uppercase; white-space: nowrap;
  }
</style>
</head>
<body>
<main class="sheet">

  <section class="card card-front" aria-label="Business card front">
    <div class="card-front__photo" role="img" aria-label="Photograph of a splash of clear blue water"></div>
    <svg class="card-front__panel" viewBox="0 0 840 480" aria-hidden="true">
      <polygon points="0,0 380,0 440,240 380,480 0,480"/>
    </svg>

    <div class="brand-lockup">
      <div class="brand-lockup__mark"></div>
      <div class="brand-lockup__name">Dorsey K. Wendell</div>
    </div>

    <div class="contact">
      <p class="contact__address">5187 W. Cedar Brook Rd.<br>Harlow Springs, PA 16924</p>
      <p class="contact__person">Russell T. Wendell</p>
      <p class="contact__phone">(717) 592-0817</p>
      <p class="contact__email">russelltwendell@fernmail.net</p>
      <p class="contact__web">dorseykwendell.net</p>
      <p class="contact__license">PA #093148</p>
    </div>
  </section>

  <section class="card card-back" aria-label="Business card back">
    <div class="card-back__band"></div>
    <div class="card-back__lockup">
      <div class="card-back__mark"></div>
      <div class="card-back__name">Dorsey K. Wendell</div>
    </div>
  </section>

</main>
</body>
</html>
```